Innovative approaches to treat addiction

PowerPoint on different techniques
Add graphics to screen
Easy to follow
I've provided the PowerPoint w content
Now make it pretty
And
hand outs for them to follow and take notes
Can you also add my bio:
Mara J. Thornquist, MS LCADC is a licensed Psychotherapist with a specialty in Addiction Disorders and over 22 years of clinical experience. Her integrative approach to counseling combines years of clinical experience with cognitive behavioral and traditional psychotherapy, with holistic therapies including; mindfulness, NLP, hypnotherapy, yoga therapy, reiki, motivational and wellness coaching.
Handout materials for them to follow and take notes

```html
<!DOCTYPE html>
<html lang="en">
<head>
<meta charset="utf-8">
<title>Innovative Techniques to Treat Disorders – Slide Set</title>
<link href="https://fonts.googleapis.com/css2?family=Arimo:wght@400;700&family=Carlito:wght@400;700&display=swap" rel="stylesheet">
<style>
  :root {
    --backdrop: #c8a77c;
    --slide-white: #ffffff;
    --brand-blue: #4f81bd;
    --deep-blue: #3b6699;
    --sky-top: #6fa6dc;
    --sky-bottom: #b9d6f1;
    --mist-blue: #c9d9ec;
    --ink: #1a1a1a;
    --heading-gray: #3c3c3c;
    --dot-gray: #dcdcdc;
    --photo-tone: #5a4a46;
    --photo-light: #cfcfd3;
  }
  * { box-sizing: border-box; margin: 0; padding: 0; }
  html, body { width: 1200px; height: 1000px; overflow: hidden; }
  body { background: var(--backdrop); position: relative; font-family: "Arimo", Arial, sans-serif; color: var(--ink); }

  .slide { position: absolute; width: 577px; height: 457px; background: var(--slide-white); overflow: hidden; }
  .slide--title { left: 20px; top: 30px; }
  .slide--bio { left: 610px; top: 30px; }
  .slide--agenda { left: 20px; top: 510px; }
  .slide--closing { left: 610px; top: 510px; background: var(--brand-blue); }

  /* Title slide */
  .title-sky { position: absolute; left: 0; top: 0; width: 100%; height: 100px;
    background: linear-gradient(180deg, var(--sky-top), var(--sky-bottom)); }
  .title-band { position: absolute; left: 0; top: 108px; width: 100%; height: 132px; background: var(--brand-blue);
    display: flex; align-items: center; justify-content: center; }
  .title-band h1 { color: #fff; font-weight: 700; font-size: 29px; line-height: 37px; text-align: center; }
  .title-fade { position: absolute; left: 0; top: 248px; width: 100%; height: 130px;
    background: linear-gradient(180deg, var(--mist-blue), var(--slide-white)); }
  .title-presenter { position: absolute; left: 0; top: 295px; width: 100%; text-align: center; color: var(--heading-gray); font-size: 16px; }
  .title-presenter strong { font-size: 21px; font-weight: 700; }
  .title-dots { position: absolute; left: 272px; top: 384px; display: flex; gap: 2px; }
  .title-dots span { width: 10px; height: 10px; border-radius: 50%; background: var(--dot-gray); }

  /* Bio slide */
  .bio-sidebar { position: absolute; left: 0; top: 0; width: 228px; height: 100%; background: var(--deep-blue); }
  .bio-portrait { position: absolute; left: 26px; top: 8px; width: 174px; height: 227px;
    background: radial-gradient(ellipse at 50% 40%, var(--photo-tone), #3b2d2b 60%, var(--photo-light) 100%);
    border: 2px solid #2e4f78; }
  .bio-name { position: absolute; left: 22px; top: 258px; color: #fff; font-size: 15px; font-weight: 700; white-space: nowrap; }
  .bio-name small { font-size: 11px; font-weight: 400; }
  .bio-rule { position: absolute; left: 0; top: 292px; width: 100%; height: 1px; background: #6b8fbb; }
  .bio-roles { position: absolute; left: 22px; top: 321px; list-style: none; color: #fff; font-family: "Carlito", Calibri, sans-serif;
    font-weight: 700; font-size: 14px; line-height: 18.5px; }
  .bio-text { position: absolute; left: 288px; top: 122px; width: 272px; font-size: 14px; line-height: 18.3px; color: #111; }
  .bio-signoff { position: absolute; left: 289px; top: 354px; width: 261px; height: 1px; background: #111; }

  /* Agenda slide */
  .agenda-header { position: absolute; left: 28px; top: 18px; width: 520px; height: 76px; background: var(--brand-blue);
    box-shadow: 3px 4px 4px rgba(0,0,0,0.3); display: flex; align-items: center; justify-content: center; }
  .agenda-header h2 { color: #fff; font-size: 27px; line-height: 36px; font-weight: 700; text-align: center; }
  .agenda-body { position: absolute; left: 35px; top: 128px; font-family: "Carlito", Calibri, sans-serif; }
  .agenda-lead { font-size: 16px; margin-bottom: 14px; }
  .agenda-list { list-style: none; font-weight: 700; font-size: 15px; line-height: 19.3px; }
  .agenda-list li { position: relative; padding-left: 21px; }
  .agenda-list li::before { content: "•"; position: absolute; left: 0; }
  .agenda-note { position: absolute; left: 35px; top: 363px; width: 510px; font-family: "Carlito", Calibri, sans-serif; font-size: 11px; line-height: 12.5px; }

  /* Closing slide */
  .closing-text { position: absolute; left: 0; top: 174px; width: 100%; text-align: center; color: #fff;
    font-family: "Carlito", Calibri, sans-serif; font-weight: 700; font-size: 40px; }
</style>
</head>
<body>

<section class="slide slide--title">
  <div class="title-sky" role="img" aria-label="Photo of a blue sky with soft white clouds"></div>
  <div class="title-band"><h1>Innovative Techniques to<br>Treat Disorders</h1></div>
  <div class="title-fade"></div>
  <p class="title-presenter"><strong>Mara Thornquist</strong>, MS LCADC, CHT, 500RYT</p>
  <div class="title-dots"><span></span><span></span><span></span></div>
</section>

<section class="slide slide--bio">
  <aside class="bio-sidebar">
    <div class="bio-portrait" role="img" aria-label="Portrait photo of the presenter"></div>
    <p class="bio-name">Mara Thornquist, <small>MS LCADC</small></p>
    <div class="bio-rule"></div>
    <ul class="bio-roles">
      <li>Phychotherapist</li>
      <li>Hypnotherapist</li>
      <li>Addiction Specialist</li>
      <li>410-555-0172</li>
    </ul>
  </aside>
  <p class="bio-text"><strong>Mara J. Thornquist, MS LCADC</strong>&nbsp; is a licensed Psychotherapist&nbsp; with a specialty in Addiction Disorders and over 22 years of clinical experience. Her integrative approach to counseling combines years of clinical experience with cognitive behavioral and traditional psychotherapy, with holistic therapies including; mindfulness, NLP, hypnotherapy, yoga therapy, reiki, motivational and wellness coaching.</p>
  <div class="bio-signoff"></div>
</section>

<section class="slide slide--agenda">
  <header class="agenda-header"><h2>New Innovative Approaches for<br>Treatment of Addiction</h2></header>
  <div class="agenda-body">
    <p class="agenda-lead">In the next hour you will learn tools that:</p>
    <ul class="agenda-list">
      <li>Increase patient retention</li>
      <li>Increase rapport</li>
      <li>Increase healing time</li>
      <li>Increase compliance with treatment recommendations</li>
      <li>Reduce stress</li>
      <li>Reduce burnout</li>
      <li>Fun and sustainable</li>
      <li>Anyone can do it!</li>
    </ul>
  </div>
  <p class="agenda-note">* These techniques are not a replacement of standard medical procedures, but works in conjunction with them by freeing the patient of feelings or attitudes that may be compromising his or her natural immune system.*</p>
</section>

<section class="slide slide--closing">
  <p class="closing-text">THANK YOU</p>
</section>

</body>
</html>
```